Business Card Design

I need a business card for my Heating / Cooling Business. I've been in the business for 28 years. The name of the company is "Tom's Heating and Cooling".
Designers, I've attached an old business card we've used to copy the information.
Take off 15 years of experience
Industry/Entity Type
Business
Contact Information for Business Card
Gene Waltham and Lorna Waltham(740)-795-4758

```html
<!DOCTYPE html>
<html lang="en">
<head>
<meta charset="utf-8">
<title>Tom's Heating &amp; Air Conditioning – Business Card</title>
<link href="https://fonts.googleapis.com/css2?family=Arimo&family=Tinos:ital,wght@1,700&display=swap" rel="stylesheet">
<style>
  :root {
    --navy: #262a6b;
    --card: #ffffff;
    --backdrop: #e9e8e4;
    --shadow: rgba(0, 0, 0, 0.18);
  }
  * { box-sizing: border-box; margin: 0; padding: 0; }
  html, body {
    width: 1200px;
    height: 900px;
    overflow: hidden;
    background: var(--backdrop);
  }
  .canvas {
    position: relative;
    width: 1200px;
    height: 900px;
  }
  .card {
    position: absolute;
    left: 285px;
    width: 630px;
    height: 360px;
    background: var(--card);
    box-shadow: 0 6px 18px var(--shadow);
    overflow: hidden;
    color: var(--navy);
    font-family: "Arimo", Arial, sans-serif;
  }
  .card--back { top: 60px; }
  .card--front { top: 480px; }
  .band {
    position: absolute;
    left: 0;
    width: 100%;
    background: var(--navy);
  }
  .band--top { top: 0; height: 14px; }
  .band--bottom { bottom: 0; height: 30px; }

  .services {
    position: absolute;
    top: 118px;
    left: 0;
    width: 100%;
    text-align: center;
    font-size: 19px;
    line-height: 1.22;
  }

  .company-name {
    position: absolute;
    top: 70px;
    left: 0;
    width: 100%;
    text-align: center;
    font-family: "Tinos", "Times New Roman", serif;
    font-style: italic;
    font-weight: 700;
    font-size: 35px;
    letter-spacing: 0.2px;
  }
  .contact {
    position: absolute;
    top: 132px;
    left: 250px;
    width: 220px;
    text-align: center;
    font-size: 19px;
    line-height: 1.22;
  }
  .address {
    position: absolute;
    top: 258px;
    left: 0;
    width: 100%;
    padding-left: 60px;
    text-align: center;
    font-size: 20px;
  }
</style>
</head>
<body>
<main class="canvas">
  <section class="card card--back" aria-label="Card back – services">
    <div class="band band--top"></div>
    <p class="services">
      Installation and Service Small Appliance Repair<br>
      Plumbing Refrigeration and Car Air Conditioning<br>
      Professional Mobile Home Installation
    </p>
    <div class="band band--bottom"></div>
  </section>

  <section class="card card--front" aria-label="Card front – contact">
    <div class="band band--top"></div>
    <h1 class="company-name">Tom's Heating &amp; Air Conditioning</h1>
    <p class="contact">
      Gene Waltham<br>
      Certified Repairman<br>
      (612) 438-2091
    </p>
    <p class="address">48120 Maple Ridge Drive Cedar Falls, Ohio 43815</p>
    <div class="band band--bottom"></div>
  </section>
</main>
</body>
</html>
```